Business card

We are looking for a creative person to deigns our company business card.

Target Market(s)

College age student

Industry/Entity Type

Accommodation

Contact Information for Business Card

We want a fun, clean and sophisticated design. It should look good, but more importantly the information should be legible.

Font styles to use
Serif
Sans Serif
Other font styles liked:
• Open Sans ,

Colors
33a6d7

Requirements
Must have
• Must have a young and memorable message. Be legible.
• Our logo on the back on a solid blue , please find color and logo attached
• LodgeNestly.com on the back.
Nice to have
• I would like to have couple of different fonts on the LodgeNestly.com on the back of the cards with a solid blue.

```html
<!DOCTYPE html>
<html lang="en">
<head>
<meta charset="utf-8">
<title>LodgeNestly Business Card</title>
<link rel="stylesheet" href="https://fonts.googleapis.com/css2?family=Open+Sans:wght@400;600;700&display=swap">
<style>
  :root {
    --canvas-bg: #e9e8e6;
    --card-white: #f8f8f6;
    --brand-navy: #0e4f86;
    --brand-blue: #33a6d7;
    --brand-mid: #1e7fc0;
    --back-deep: #0a5a96;
    --back-light: #2a8fd0;
    --text-dark: #2b2b2b;
    --rule: #b9b9b9;
  }
  * { box-sizing: border-box; margin: 0; padding: 0; }
  html, body {
    width: 1200px; height: 844px; overflow: hidden;
    background: var(--canvas-bg);
    font-family: "Open Sans", sans-serif;
  }
  .stage {
    position: relative; width: 1200px; height: 844px;
    display: flex; align-items: center; justify-content: center; gap: 50px;
  }
  .card {
    position: relative; width: 520px; height: 300px;
    border-radius: 2px;
    box-shadow: 0 6px 18px rgba(0,0,0,0.18);
  }
  /* Front */
  .card-front { background: var(--card-white); color: var(--text-dark); }
  .front-brand {
    position: absolute; right: 60px; top: 48px;
    display: flex; flex-direction: column; align-items: center; gap: 10px;
  }
  .front-brand .brand-square {
    width: 38px; height: 38px; background: var(--brand-blue);
  }
  .front-brand .brand-name {
    font-weight: 700; font-size: 22px; color: var(--brand-navy); letter-spacing: -0.3px;
  }
  .rule {
    position: absolute; left: 28px; right: 28px; height: 1px; background: var(--rule);
  }
  .rule-top { top: 126px; left: 150px; }
  .rule-mid { top: 150px; }
  .rule-low { top: 218px; }
  .person { position: absolute; left: 28px; top: 164px; }
  .person-name { font-weight: 700; font-size: 20px; line-height: 1.1; }
  .person-name .first { color: var(--brand-navy); }
  .person-name .last { color: var(--brand-blue); }
  .person-role { font-size: 13px; margin-top: 2px; }
  .web-front {
    position: absolute; right: 30px; top: 194px;
    font-weight: 700; font-size: 12px; color: var(--brand-mid);
  }
  .contact {
    position: absolute; left: 28px; top: 228px;
    font-size: 13px; line-height: 1.9;
  }
  .contact .label { font-weight: 700; color: var(--brand-mid); }
  .contact .gap { display: inline-block; width: 18px; }
  /* Back */
  .card-back {
    background: radial-gradient(ellipse at 45% 40%, var(--back-light) 0%, var(--brand-mid) 45%, var(--back-deep) 100%);
    color: #fff;
    display: flex; flex-direction: column; align-items: center; justify-content: center;
  }
  .back-brand { display: flex; align-items: center; gap: 14px; }
  .back-brand .brand-square { width: 44px; height: 44px; background: #fff; }
  .back-brand .brand-name { font-weight: 700; font-size: 34px; letter-spacing: -0.5px; }
  .web-back { margin-top: 26px; font-weight: 700; font-size: 13px; letter-spacing: 0.5px; }
</style>
</head>
<body>
<main class="stage">
  <section class="card card-front" aria-label="Business card front">
    <div class="front-brand">
      <span class="brand-square"></span>
      <span class="brand-name">LodgeNestly</span>
    </div>
    <div class="rule rule-top"></div>
    <div class="rule rule-mid"></div>
    <div class="person">
      <p class="person-name"><span class="first">Daniel</span> <span class="last">Reyes</span></p>
      <p class="person-role">Managing Director</p>
    </div>
    <p class="web-front">www.lodgenestly.com</p>
    <div class="rule rule-low"></div>
    <div class="contact">
      <p>1234, Address GoesHere, Country, 12345</p>
      <p><span class="label">P:</span> (044)987650321<span class="gap"></span><span class="label">E:</span> hello@lodgenestly.com</p>
    </div>
  </section>

  <section class="card card-back" aria-label="Business card back">
    <div class="back-brand">
      <span class="brand-square"></span>
      <span class="brand-name">LodgeNestly</span>
    </div>
    <p class="web-back">www.lodgenestly.com</p>
  </section>
</main>
</body>
</html>
```